Maple Ridge Hops Farm

We need a business card with some pizam in it. Our slogan is something different so something a little different would do!

Business

```html
<!DOCTYPE html>
<html lang="en">
<head>
<meta charset="utf-8">
<title>Maple Ridge Hops Farm – Business Card</title>
<link rel="stylesheet" href="https://fonts.googleapis.com/css2?family=Nunito:wght@400;600;700;800&display=swap">
<style>
  :root {
    --olive: #5e602d;
    --olive-icon: #66652b;
    --pill-grey: #c2c2c2;
    --pill-ghost: rgba(235, 235, 235, 0.55);
    --card-paper: #f4f4f3;
    --ink: #1e1e1e;
    --ink-soft: #2c2c2c;
    --white: #ffffff;
    --page: #ffffff;
  }
  * { box-sizing: border-box; margin: 0; padding: 0; }
  html, body {
    width: 1200px;
    height: 1000px;
    overflow: hidden;
    background: var(--page);
    font-family: "Nunito", sans-serif;
  }
  .canvas { position: relative; width: 1200px; height: 1000px; }

  .card {
    position: absolute;
    top: 93px;
    width: 483px;
    height: 827px;
    overflow: hidden;
    box-shadow: 2px 3px 6px rgba(0, 0, 0, 0.28);
  }
  .card--front { left: 108px; }
  .card--back { left: 622px; background: var(--card-paper); }

  .card__band-top {
    position: absolute; left: 0; top: 0; width: 100%; height: 43px;
    background: var(--olive); z-index: 3;
  }
  .card__band-bottom {
    position: absolute; left: 0; bottom: 0; width: 100%; height: 43px;
    background: var(--olive); z-index: 3;
    display: flex; align-items: center; justify-content: center;
  }
  .tagline {
    color: var(--white);
    font-weight: 700;
    font-size: 21px;
    letter-spacing: 4px;
  }

  .field-photo {
    position: absolute; left: 0; top: 43px; width: 100%; height: 741px;
    background: linear-gradient(180deg,
      #d9dde2 0%, #e6e8ea 38%, #dfe2e3 48%,
      #2f5a2a 52%, #3b6a31 70%, #4d6b36 82%, #6a5a45 88%, #5b4a3a 100%);
  }

  .brand {
    position: absolute; left: 0; width: 100%;
    text-align: center; z-index: 2;
    display: flex; flex-direction: column; align-items: center; gap: 10px;
  }
  .brand--front { top: 108px; }
  .brand--back { top: 112px; }
  .brand__mark {
    width: 26px; height: 26px; border-radius: 50%;
    background: var(--olive);
  }
  .brand__name {
    color: var(--olive);
    font-weight: 800;
    font-size: 44px;
    line-height: 1.02;
    letter-spacing: 1px;
    text-transform: uppercase;
  }
  .brand--front .brand__name { color: var(--olive); }

  .person-name {
    position: absolute; left: 22px; top: 350px;
    font-weight: 700; font-size: 34px; color: var(--ink);
  }

  .contact-list { list-style: none; }
  .contact {
    position: absolute; left: 0; width: 358px; height: 62px;
    background: var(--pill-grey);
    border-radius: 0 20px 20px 0;
    display: flex; align-items: center;
  }
  .contact__icon {
    width: 96px; display: flex; justify-content: center; align-items: center;
  }
  .contact__text {
    font-size: 19px; color: var(--ink-soft); line-height: 1.25;
    font-weight: 400;
  }
  .contact--phone { top: 426px; }
  .contact--email { top: 515px; }
  .contact--social { top: 604px; }
  .contact--address { top: 695px; }

  .ghost-tab {
    position: absolute; left: 417px; width: 80px; height: 62px;
    background: var(--pill-ghost);
    border-radius: 20px 0 0 20px;
    z-index: 2;
  }
  .ghost-tab--1 { top: 426px; }
  .ghost-tab--2 { top: 515px; }
  .ghost-tab--3 { top: 604px; }
  .ghost-tab--4 { top: 695px; }

  .social-square {
    width: 28px; height: 28px; background: var(--olive-icon);
  }
</style>
</head>
<body>
<div class="canvas">

  <section class="card card--front" aria-label="Card front">
    <div class="card__band-top"></div>
    <div class="field-photo" role="img" aria-label="Photograph of a hop yard with tall wooden poles and strung wires in front of a wooded hillside under an overcast sky"></div>
    <div class="brand brand--front">
      <span class="brand__mark"></span>
      <span class="brand__name">Maple Ridge<br>Hops Farm</span>
    </div>
    <div class="ghost-tab ghost-tab--1"></div>
    <div class="ghost-tab ghost-tab--2"></div>
    <div class="ghost-tab ghost-tab--3"></div>
    <div class="ghost-tab ghost-tab--4"></div>
    <div class="card__band-bottom"><span class="tagline">something different</span></div>
  </section>

  <section class="card card--back" aria-label="Card back">
    <div class="card__band-top"></div>
    <div class="brand brand--back">
      <span class="brand__mark"></span>
      <span class="brand__name">Maple Ridge<br>Hops Farm</span>
    </div>
    <h1 class="person-name">Daniel Whitaker</h1>
    <ul class="contact-list">
      <li class="contact contact--phone">
        <span class="contact__icon">
          <svg width="22" height="40" viewBox="0 0 22 40" aria-hidden="true">
            <rect x="1.5" y="1.5" width="19" height="37" rx="3" fill="none" stroke="var(--olive-icon)" stroke-width="3"/>
            <line x1="3" y1="8" x2="19" y2="8" stroke="var(--olive-icon)" stroke-width="2"/>
            <line x1="3" y1="31" x2="19" y2="31" stroke="var(--olive-icon)" stroke-width="2"/>
            <circle cx="11" cy="35" r="1.6" fill="var(--olive-icon)"/>
          </svg>
        </span>
        <span class="contact__text">5550142817</span>
      </li>
      <li class="contact contact--email">
        <span class="contact__icon">
          <svg width="36" height="24" viewBox="0 0 36 24" aria-hidden="true">
            <rect x="0" y="0" width="36" height="24" fill="var(--olive-icon)"/>
            <polyline points="0,0 18,13 36,0" fill="none" stroke="var(--pill-grey)" stroke-width="2"/>
          </svg>
        </span>
        <span class="contact__text">dwhitaker7@mailbox.com</span>
      </li>
      <li class="contact contact--social">
        <span class="contact__icon"><span class="social-square"></span></span>
        <span class="contact__text">mapleridgehopsfarm</span>
      </li>
      <li class="contact contact--address">
        <span class="contact__icon">
          <svg width="24" height="36" viewBox="0 0 24 36" aria-hidden="true">
            <path d="M12 0C5.4 0 0 5.3 0 11.9 0 20.5 12 36 12 36S24 20.5 24 11.9C24 5.3 18.6 0 12 0Z" fill="var(--olive-icon)"/>
            <circle cx="12" cy="11.5" r="4.5" fill="var(--pill-grey)"/>
          </svg>
        </span>
        <span class="contact__text">4120 Orchard Lane,<br>Milltown, NY 14000</span>
      </li>
    </ul>
    <div class="card__band-bottom"><span class="tagline">something different</span></div>
  </section>

</div>
</body>
</html>
```